Web Design Project

we require new design / layout for www.sturdicanopy.eu design clean easy read must send strong and industrial theme as selling point to our product is the strength in our products

To include step process for the www.sturdicanopy.eu/designer2

For step process have similar layout to http://www.shirtlodge.com/create/own_temp.php

Industry/Entity Type

Industrial

```html
<!DOCTYPE html>
<html lang="en">
<head>
<meta charset="utf-8">
<title>Sturdicanopy – Strong Pop Up Tents</title>
<link rel="stylesheet" href="https://fonts.googleapis.com/css2?family=Michroma&display=swap">
<style>
  :root {
    --navy: #13319a;
    --red: #ee1c1c;
    --page: #efeeec;
    --panel: #fafafa;
    --ink: #222222;
    --muted: #6b6b6b;
    --grey-bar: #a9a9a9;
    --white: #ffffff;
    --hero-sky: #8ea0c4;
    --hero-grass: #5f7f40;
    --display: "Michroma", sans-serif;
    --body: Arial, Helvetica, sans-serif;
  }
  * { box-sizing: border-box; margin: 0; padding: 0; }
  html, body { width: 1064px; height: 1200px; overflow: hidden; }
  body { background: var(--page); font-family: var(--body); color: var(--ink); position: relative; }

  .logo { position: absolute; display: flex; align-items: center; gap: 7px; font-family: var(--display); color: var(--navy); }
  .logo .mark { width: 10px; height: 10px; background: var(--red); }
  .logo--header { left: 128px; top: 36px; font-size: 17px; }
  .logo--footer { left: 778px; top: 1047px; font-size: 13px; }

  .utility-bar { position: absolute; left: 642px; top: 30px; width: 297px; height: 22px; background: var(--grey-bar); color: var(--white);
    font-size: 11.5px; letter-spacing: .3px; display: flex; align-items: center; gap: 12px; padding-left: 18px; }
  .utility-bar .cart::before { content: ""; display: inline-block; width: 10px; height: 7px; border: 1.5px solid var(--white); border-top: 0; margin-right: 5px; }
  .utility-bar .flag { display: inline-block; width: 12px; height: 8px; background: linear-gradient(#b22 50%, #fff 50%); margin-left: 3px; vertical-align: -1px; }

  .main-nav { position: absolute; left: 0; top: 73px; width: 1064px; height: 58px; background: var(--navy); }
  .main-nav ul { list-style: none; position: absolute; left: 128px; top: 19px; display: flex; gap: 26px; }
  .main-nav a { color: var(--white); font-family: var(--display); font-size: 14px; text-decoration: none; padding-bottom: 5px; }
  .main-nav a.current { border-bottom: 2px solid var(--white); }
  .search { position: absolute; left: 528px; top: 19px; width: 156px; height: 20px; background: var(--white); color: #aaa; font-size: 10px; padding: 4px 11px; }
  .search svg { position: absolute; right: 6px; top: 5px; }
  .nav-phone { position: absolute; left: 705px; top: 18px; color: var(--white); font-family: var(--display); font-size: 19px; display: flex; align-items: center; gap: 5px; white-space: nowrap; }

  .hero { position: absolute; left: 0; top: 131px; width: 1064px; height: 384px; background: #f1f0ee; box-shadow: 0 4px 6px rgba(0,0,0,.25); overflow: hidden; }
  .hero-photo { position: absolute; left: 430px; top: 0; width: 634px; height: 384px;
    background:
      linear-gradient(to right, #f1f0ee 0%, rgba(241,240,238,0) 30%),
      linear-gradient(to bottom, var(--hero-sky) 0%, #9aa79a 50%, var(--hero-grass) 100%); }
  .hero h1 { position: absolute; left: 125px; top: 96px; font-family: var(--display); font-weight: 400; color: var(--navy); font-size: 31px; line-height: 33px; white-space: nowrap; }
  .hero p { position: absolute; left: 125px; top: 180px; width: 490px; font-size: 17px; line-height: 21px; color: var(--ink); }
  .btn { position: absolute; display: flex; align-items: center; justify-content: center; gap: 10px; color: var(--white); font-family: var(--display); font-size: 14px; text-decoration: none; white-space: nowrap; }
  .btn .go { width: 15px; height: 15px; border-radius: 50%; background: var(--white); display: inline-flex; align-items: center; justify-content: center; }
  .btn--blue { background: var(--navy); }
  .btn--blue .go svg { fill: var(--navy); }
  .btn--red { background: var(--red); }
  .btn--red .go svg { fill: var(--red); }
  .hero .btn--blue { left: 125px; top: 242px; width: 162px; height: 36px; }
  .hero .btn--red { left: 295px; top: 242px; width: 162px; height: 36px; }

  .content { position: absolute; left: 125px; top: 568px; width: 814px; height: 427px; background: var(--panel); }
  .categories { position: absolute; left: 0; top: 0; width: 212px; height: 427px; background: var(--red); color: var(--white); }
  .categories h2 { font-family: var(--display); font-weight: 400; font-size: 17px; line-height: 20px; margin: 22px 0 0 24px; }
  .categories ul { list-style: none; margin-top: 21px; }
  .categories li { height: 25.8px; border-bottom: 1px dotted rgba(255,255,255,.45); font-size: 12.5px; letter-spacing: .3px; padding: 5px 0 0 43px; position: relative; }
  .categories li:last-child { border-bottom: 0; }
  .categories li::before { content: "+"; position: absolute; left: 27px; top: 6px; width: 9px; height: 9px; border-radius: 50%; background: var(--white); color: var(--red); font-size: 9px; line-height: 9px; text-align: center; font-weight: bold; }

  .intro h2 { position: absolute; left: 231px; top: 34px; font-family: var(--display); font-weight: 400; font-size: 15.5px; color: var(--ink); white-space: nowrap; }
  .intro .copy { position: absolute; left: 233px; top: 85px; width: 275px; font-size: 10.4px; line-height: 12.3px; color: var(--muted); }
  .intro .copy p { margin-bottom: 12px; }
  .learn-more { position: absolute; left: 231px; top: 387px; width: 91px; height: 16px; background: var(--red); color: var(--white); font-size: 10px; text-align: center; line-height: 16px; letter-spacing: .3px; text-decoration: none; }

  .tile { position: absolute; left: 519px; width: 267px; height: 91px; box-shadow: 0 4px 5px rgba(0,0,0,.2); color: var(--white); overflow: hidden; text-decoration: none; }
  .tile h3 { font-family: var(--display); font-weight: 400; font-size: 14px; line-height: 19px; }
  .tile--design { top: 83px; background: linear-gradient(to right, #a39a8a, #b7ad9b 70%, #a79e8c); }
  .tile--design .thumb { position: absolute; left: 0; top: 0; width: 98px; height: 91px; background: linear-gradient(to bottom, #8fa66a, #4d6a34); }
  .tile--design h3 { position: absolute; left: 120px; top: 27px; }
  .tile--design .arrow { position: absolute; right: 12px; bottom: 10px; width: 18px; height: 18px; border-radius: 50%; background: #eee; display: flex; align-items: center; justify-content: center; }
  .tile--why { top: 198px; background: linear-gradient(to bottom, #9a8a66, #5b4a2c); }
  .tile--why h3 { position: absolute; left: 13px; top: 25px; color: #141414; }
  .tile--why p { position: absolute; left: 13px; top: 55px; font-size: 12px; line-height: 15px; }
  .tile--secure { top: 310px; left: 517px; background: linear-gradient(to bottom, #e0584e, #c23428); }
  .tile--secure svg { position: absolute; left: 15px; top: 12px; }
  .tile--secure h3 { position: absolute; left: 82px; top: 27px; }

  .footer-links { position: absolute; top: 1033px; list-style: none; font-size: 11px; color: var(--ink); }
  .footer-links li { height: 23.6px; }
  .footer-links--a { left: 127px; }
  .footer-links--b { left: 238px; }
  .tollfree { position: absolute; left: 396px; top: 1033px; display: flex; gap: 5px; }
  .tollfree small { display: block; font-size: 11px; line-height: 11px; }
  .tollfree strong { display: block; font-family: var(--display); font-weight: 400; font-size: 15px; white-space: nowrap; }
  .social { position: absolute; left: 395px; top: 1072px; display: flex; gap: 7px; }
  .social span { width: 33px; height: 33px; border-radius: 50%; background: #a8a8a8; }
  .footer-cta { left: 397px; top: 1114px; width: 162px; height: 36px; }
  .payment h4 { position: absolute; left: 625px; top: 1031px; font-family: var(--display); font-weight: 400; font-size: 13.5px; line-height: 19px; }
  .payment .badges { position: absolute; left: 625px; top: 1081px; display: grid; grid-template-columns: 55px 55px; gap: 3px 3px; }
  .payment .badges span { height: 32px; border-radius: 2px; background: #e6e6ea; }
  .payment .badges span:nth-child(3) { background: #2b4f9b; }
  .payment .badges span:nth-child(4) { background: #2d5fa5; }
  .copyright { position: absolute; left: 778px; top: 1079px; font-size: 11px; line-height: 13px; }
</style>
</head>
<body>
  <header>
    <div class="logo logo--header"><span class="mark"></span>sturdicanopy.eu</div>
    <div class="utility-bar">
      <span>MY ACCOUNT</span>
      <span class="cart">SHOPPING CART</span>
      <span>▾ US<span class="flag"></span></span>
    </div>
    <nav class="main-nav">
      <ul>
        <li><a href="#">Home</a></li>
        <li><a href="#" class="current">Products</a></li>
        <li><a href="#">FAQ</a></li>
        <li><a href="#">Contact</a></li>
      </ul>
      <div class="search">Search
        <svg width="10" height="10" viewBox="0 0 10 10"><circle cx="4" cy="4" r="3" fill="none" stroke="#bbb" stroke-width="1.3"/><line x1="6.2" y1="6.2" x2="9" y2="9" stroke="#bbb" stroke-width="1.3"/></svg>
      </div>
      <div class="nav-phone">
        <svg width="11" height="18" viewBox="0 0 12 20"><path d="M4 1 L8 1 L8 5 L5 6 Q4 10 5 14 L8 15 L8 19 L4 19 Q0 10 4 1 Z" fill="#fff"/></svg>
        0800 61 72 830
      </div>
    </nav>
  </header>

  <section class="hero">
    <div class="hero-photo" role="img" aria-label="Photo of a family picnicking under a blue pop up canopy in a park by the water"></div>
    <h1>THE STRONGEST<br>CANOPIES IN WORLD</h1>
    <p>Lorem ipsum dolor sit amet, consectetur lorem ipsum incidid unt labore magna ipsum sit dolor</p>
    <a class="btn btn--blue" href="#">Get in Touch <span class="go"><svg width="9" height="9" viewBox="0 0 9 9"><path d="M1 3.5h4V1.5l3 3-3 3v-2H1z"/></svg></span></a>
    <a class="btn btn--red" href="#">Join Services <span class="go"><svg width="9" height="9" viewBox="0 0 9 9"><path d="M1 3.5h4V1.5l3 3-3 3v-2H1z"/></svg></span></a>
  </section>

  <main class="content">
    <aside class="categories">
      <h2>Product<br>Categories</h2>
      <ul>
        <li>2m x 2m Canopies</li>
        <li>3m x 3m Canopies</li>
        <li>3m x 4.5m Canopies</li>
        <li>3m x 6m Canopies</li>
        <li>4m x 4m Oriental Tents</li>
        <li>5m x 5m Oriental Tents</li>
        <li>Clear Walls</li>
        <li>Gutters</li>
        <li>Parts</li>
        <li>Roof</li>
        <li>Sandbags</li>
        <li>Tables</li>
        <li>Walls</li>
      </ul>
    </aside>

    <article class="intro">
      <h2>Sturdicanopy offers pop up gazebos for sale near you</h2>
      <div class="copy">
        <p>Pop up gazebos for sale near you! We at Sturdicanopy have been able to expand our markets to different countries and our pop up gazebos are now available for delivery in several European countries, so your wait is over. All you have to do now is order your instant awnings from our website Sturdicanopy.eu Please note that we deliver to the UK , Ireland, Europe</p>
        <p>Our pop up gazebos are the best on the web and are durable enough to last for years. Sturdicanopy offer a large range of coloured mini marquees, heavy duty gazebos and instant awnings and aims to satisfy its customers by providing them with the best quality products. All our pop up marquees are available on our website and you can order them right away!</p>
        <p>Heavy Duty Instant Awnings</p>
        <p>Our pop-up gazebos are produced with the best quality material so there is no chance of them breaking easily. The 40mm wide poles are made from the best quality, strong and durable aluminium and have strong bolts which guarantee best quality.</p>
      </div>
      <a class="learn-more" href="#">LEARN MORE</a>
    </article>

    <a class="tile tile--design" href="#">
      <div class="thumb" role="img" aria-label="Photo of a black pop up tent with side walls on a lawn"></div>
      <h3>DESIGN YOUR<br>OWN TENT</h3>
      <span class="arrow"><svg width="9" height="9" viewBox="0 0 9 9"><path d="M1 3.5h4V1.5l3 3-3 3v-2H1z" fill="#777"/></svg></span>
    </a>
    <a class="tile tile--why" href="#" role="img" aria-label="Blurred photo of an outdoor event under canopies">
      <h3>WHY BUY FROM US</h3>
      <p>Lorem ipsum dolor sit amet consectetur amet<br>Adipisicing elit amet, consectetur</p>
    </a>
    <a class="tile tile--secure" href="#">
      <svg width="50" height="70" viewBox="0 0 50 70"><path d="M13 32V22a12 12 0 0 1 24 0v10" fill="none" stroke="#fff" stroke-width="5"/><circle cx="25" cy="48" r="20" fill="none" stroke="#fff" stroke-width="4"/><circle cx="25" cy="45" r="4" fill="#fff"/><rect x="23.5" y="45" width="3" height="9" fill="#fff"/></svg>
      <h3>100% SECURE<br>SHOPPING</h3>
    </a>
  </main>

  <footer>
    <ul class="footer-links footer-links--a">
      <li>Home</li><li>FAQ</li><li>About Us</li><li>Instructions</li><li>Privacy</li>
    </ul>
    <ul class="footer-links footer-links--b">
      <li>Delivery</li><li>Payment &amp; Returns</li><li>Terms &amp; Conditions</li><li>Contact Us</li><li>Tent Templates</li>
    </ul>
    <div class="tollfree">
      <svg width="12" height="26" viewBox="0 0 12 26"><path d="M4 1 L9 1 L9 6 L5 7 Q4 13 5 19 L9 20 L9 25 L4 25 Q-1 13 4 1 Z" fill="#222"/></svg>
      <div><small>TOLLFREE</small><strong>0800 61 72 830</strong></div>
    </div>
    <div class="social"><span></span><span></span><span></span><span></span></div>
    <a class="btn btn--blue footer-cta" href="#">Get in Touch <span class="go"><svg width="9" height="9" viewBox="0 0 9 9"><path d="M1 3.5h4V1.5l3 3-3 3v-2H1z"/></svg></span></a>
    <div class="payment">
      <h4>Payment and<br>Security with</h4>
      <div class="badges"><span></span><span></span><span></span><span></span></div>
    </div>
    <div class="logo logo--footer"><span class="mark"></span>sturdicanopy.eu</div>
    <p class="copyright">All Right Reserved © 2013</p>
  </footer>
</body>
</html>
```